Water Management Company Letterhead

Looking for a eye-catching design of letterhead for a California based parent company of water management products. The letterhead would need to include the three logos of the sub-companies, with "The Brookline Holdings LLC" (parent company) being the primary focus. Please include the sub-company logos in the following order of significance: Velomir, Drifting Meadows North, and then Tundrel Co NE. The color schemes should convey water/enviornment - blues and greens. Most importantly it should be something that will stand out. All logos are uploaded. Thank you for your interest!

Target Market(s)

Environmental conservationists, government agencies, etc.

Industry/Entity Type

Environment

Font styles to use
Serif
Sans Serif

Colors
33a6d7
3276b5
abd037
cadf82
85cae6
85acd3

Requirements
Must have
• eye-catching, blue and green tones pulled from logos, water droplet.

```html
<!DOCTYPE html>
<html lang="en">
<head>
<meta charset="utf-8">
<title>The Brookline Holdings LLC — Letterhead</title>
<link rel="stylesheet" href="https://fonts.googleapis.com/css2?family=Cormorant+SC:wght@500;600&family=Open+Sans:wght@400;600;700&display=swap">
<style>
  :root {
    --blue-deep: #3276b5;
    --blue: #2a8bc8;
    --blue-bright: #33a6d7;
    --blue-soft: #85cae6;
    --green: #8fc03c;
    --green-soft: #cadf82;
    --ink: #2b2b2b;
    --ink-soft: #555;
    --backdrop: #ececec;
    --paper: #ffffff;
    --watermark: #f4f5f6;
  }
  * { box-sizing: border-box; margin: 0; padding: 0; }
  html, body { width: 1200px; height: 1000px; overflow: hidden; }
  body {
    background: var(--backdrop);
    font-family: "Open Sans", Arial, sans-serif;
    color: var(--ink);
  }
  .letterhead {
    position: absolute;
    left: 229px; top: 20px;
    width: 742px; height: 960px;
    background: var(--paper);
    box-shadow: 0 6px 24px rgba(0,0,0,.15);
    overflow: hidden;
  }
  .top-band { position: absolute; left: 0; top: 0; width: 742px; height: 60px; }
  .brand {
    position: absolute; left: 56px; top: 96px;
    display: flex; align-items: center; gap: 10px;
  }
  .brand-dot { width: 16px; height: 16px; border-radius: 50%; background: var(--blue-bright); }
  .brand-name {
    font-family: "Cormorant SC", Georgia, serif;
    font-weight: 600; font-size: 30px; letter-spacing: .5px; color: #3a3a3a;
  }
  .contact {
    position: absolute; right: 56px; top: 40px;
    list-style: none; font-size: 10px; line-height: 14px; color: var(--ink-soft);
  }
  .contact li { display: flex; align-items: center; gap: 6px; }
  .contact .icon {
    width: 11px; height: 11px; background: var(--blue); border-radius: 2px;
  }
  .contact .indent { padding-left: 17px; }
  .watermark-circle {
    position: absolute; left: 250px; top: 300px;
    width: 260px; height: 260px; border-radius: 50%;
    background: var(--watermark);
  }
  .recipient {
    position: absolute; left: 56px; top: 172px;
    font-size: 12.5px; font-weight: 700; line-height: 19px;
  }
  .recipient .label { font-weight: 600; }
  .letter-body {
    position: absolute; left: 56px; top: 264px; width: 600px;
    font-size: 12.5px; line-height: 20px; color: #333;
  }
  .letter-body p { margin-bottom: 20px; }
  .sign-off {
    position: absolute; left: 56px; top: 580px;
    font-size: 12.5px; color: #333;
  }
  .signature {
    width: 150px; height: 52px; margin: 8px 0 6px;
    background: linear-gradient(90deg, #e9e9e9, #f5f5f5);
    border-radius: 4px;
  }
  .bottom-swoosh { position: absolute; left: 0; bottom: 0; width: 742px; height: 300px; }
  .partner {
    position: absolute; display: flex; align-items: center; gap: 6px;
    font-weight: 600; font-size: 13px; line-height: 16px;
    color: var(--blue-deep); white-space: nowrap;
  }
  .partner .mark { width: 10px; height: 10px; border-radius: 50%; background: var(--blue-bright); }
  .partner-primary { left: 360px; top: 728px; font-size: 15px; }
  .partner-second { left: 486px; top: 690px; }
  .partner-third { left: 616px; top: 650px; }
</style>
</head>
<body>
<main class="letterhead">
  <svg class="top-band" viewBox="0 0 742 60" preserveAspectRatio="none" aria-hidden="true">
    <path d="M0 30 C250 22 500 10 742 0 V6 C500 16 250 28 0 38 Z" fill="var(--blue)"/>
  </svg>

  <header>
    <div class="brand">
      <span class="brand-dot"></span>
      <span class="brand-name">The Brookline Holdings LLC</span>
    </div>
    <ul class="contact">
      <li><span class="icon"></span>(000) 555-0142</li>
      <li><span class="icon"></span>sales@brooklinehold.com</li>
      <li><span class="icon"></span>www.brooklinehold.com</li>
      <li><span class="icon"></span>Address Line 1 Street</li>
      <li class="indent">Area Name Calder, CA 90000</li>
    </ul>
  </header>

  <div class="watermark-circle" aria-hidden="true"></div>

  <section class="recipient">
    <div class="label">To</div>
    <div>Lorem Ipsum is simply</div>
    <div>Lorem Ipsum is Lorem Ipsum is</div>
    <div>Lorem Ipsum is</div>
  </section>

  <section class="letter-body">
    <p>dummy text of the printing and typesetting industry. Lorem Ipsum has been the industry's standard dummy text ever since the 1500s, when an unknown printer took a galley of type and scrambled it to make a type specimen book. It has survived not only five centuries, but also the leap into electronic typesetting, remaining essentially unchanged.</p>
    <p>It is a long established fact that a reader will be distracted by the readable content of a page when looking at its layout. The point of using Lorem Ipsum is that it has a more-or-less normal distribution of letters, as opposed to using 'Content here, content here', making it look like readable English. Many desktop publishing packages and web page editors now use Lorem Ipsum as their default model text, and a search for 'lorem .</p>
    <p>Contrary to popular belief, Lorem Ipsum is not simply random text. It has roots in a piece of classical Latin literature from 45 BC, making it over 2000 years old. Elias Marrow, a Latin professor at Ashford Vale College in Oregon, looked up one of the more obscure Latin words, consectetur, from a Lorem Ipsum passage,</p>
  </section>

  <section class="sign-off">
    <div>Lorem Ipsum</div>
    <div class="signature" role="img" aria-label="Handwritten signature"></div>
    <div>Lorem Ipsum is a dummy</div>
  </section>

  <svg class="bottom-swoosh" viewBox="0 0 742 300" preserveAspectRatio="none" aria-hidden="true">
    <path d="M0 262 C240 250 500 200 742 70 V300 H0 Z" fill="var(--blue)"/>
    <path d="M0 276 C240 266 500 214 742 90 V300 H0 Z" fill="var(--paper)"/>
    <path d="M0 282 C240 272 500 222 742 100 V300 H0 Z" fill="var(--green)"/>
    <path d="M0 292 C240 282 500 236 742 118 V300 H0 Z" fill="var(--blue)"/>
  </svg>

  <div class="partner partner-primary"><span class="mark"></span>Velomir</div>
  <div class="partner partner-second"><span class="mark"></span>Drifting Meadows North</div>
  <div class="partner partner-third"><span class="mark"></span>Tundrel Co NE</div>
</main>
</body>
</html>
```